Professional violinist needs business cards

I am trying to attract the following jobs:
-private violin lessons (primarily classical)
-performance gigs (weddings, birthday parties, funerals, etc.)
-collaborations with other artists (studio recordings, performances)

I want to communicate that I have a very high standard of excellence for my work, but I also love people and celebrations.
Values/style words I like are:
love, joy, peace, fun, beauty, authenticity, excellence, warmth, refined/sleek, free spirited. If that's too confusing, just ignore :)

I will attach my favorite business card template that I could find on Canva. The lines are supposed to be like a music staff, which I think is really cool, but I also don't want it to look too busy. I like the simple black and white--I think it looks sharp--but I also am open to other ideas. I also have seen business cards with pictures included that looked great, so I attached an image that could be used as well.

I am also attaching a file that I made of my initials that could be used as a logo, but I'm not sure if it should be included.

Information on the card:
-My name (18 letters total)
-"violinist"
-phone number, email, website

Thank you!

```html
<!DOCTYPE html>
<html lang="en">
<head>
<meta charset="UTF-8">
<title>Miriam Holloway – Violinist Business Card</title>
<link rel="stylesheet" href="https://fonts.googleapis.com/css2?family=Poppins:wght@400;500;700&family=Rubik:wght@900&display=swap">
<style>
  :root {
    --page: #ffffff;
    --card: #000000;
    --accent: #fff33b;
    --ink: #ffffff;
    --icon-ink: #000000;
  }
  * { margin: 0; padding: 0; box-sizing: border-box; }
  html, body { width: 1200px; height: 1200px; overflow: hidden; background: var(--page); }
  body { position: relative; font-family: "Poppins", sans-serif; color: var(--ink); }

  .card {
    position: absolute;
    left: 213px;
    width: 781px;
    height: 447px;
    background: var(--card);
    border-radius: 31px;
    overflow: hidden;
  }
  .card--front { top: 68px; }
  .card--back { top: 672px; }

  .violin-art {
    position: absolute;
    background: var(--accent);
    border-radius: 90px 90px 60px 60px;
  }
  .card--front .violin-art { left: 529px; top: 6px; width: 192px; height: 436px; }
  .card--back .violin-art { left: 28px; top: 6px; width: 191px; height: 434px; }

  .contact-icon {
    position: absolute;
    left: 83px;
    width: 46px;
    height: 46px;
    background: var(--ink);
    border-radius: 10px;
    display: flex;
    align-items: center;
    justify-content: center;
  }
  .contact-icon svg { width: 28px; height: 28px; }

  .name {
    position: absolute;
    left: 142px;
    top: 114px;
    font-family: "Rubik", sans-serif;
    font-weight: 900;
    font-size: 25px;
    letter-spacing: 0.3px;
    line-height: 1;
    white-space: nowrap;
  }
  .role { position: absolute; left: 143px; top: 141px; font-size: 19.5px; line-height: 1; }
  .contact-text { position: absolute; font-size: 18px; line-height: 1; letter-spacing: 0.3px; white-space: nowrap; }
  .contact-text--email { left: 142px; top: 187px; }
  .contact-text--phone { left: 152px; top: 240px; font-size: 16.5px; line-height: 20px; }
  .contact-text--web { left: 152px; top: 317px; }

  .services {
    position: absolute;
    left: 262px;
    top: 103px;
    width: 440px;
    text-align: center;
  }
  .services__title {
    font-weight: 500;
    font-size: 20px;
    line-height: 24px;
    letter-spacing: 2px;
    margin-bottom: 13px;
  }
  .service { margin-bottom: 21px; }
  .service:nth-of-type(2) { margin-bottom: 29px; }
  .service__name { font-weight: 700; font-size: 18px; line-height: 20px; letter-spacing: 0.3px; white-space: nowrap; }
  .service__detail { font-size: 17.5px; line-height: 21px; letter-spacing: 0.3px; }
</style>
</head>
<body>

  <section class="card card--front">
    <div class="violin-art" role="img" aria-label="Yellow silhouette of a violin merged with a treble clef over diagonal music staff lines"></div>

    <div class="contact-icon" style="top:112px">
      <svg viewBox="0 0 24 24" aria-hidden="true"><circle cx="12" cy="8" r="4" fill="#000"/><path d="M4 20c0-4.5 3.5-7 8-7s8 2.5 8 7z" fill="#000"/></svg>
    </div>
    <h1 class="name">MIRIAM HOLLOWAY</h1>
    <p class="role">Violinist</p>

    <div class="contact-icon" style="top:175px">
      <svg viewBox="0 0 24 24" aria-hidden="true"><rect x="2" y="5" width="20" height="14" rx="1.5" fill="#000"/><path d="M3 6.5l9 6 9-6" fill="none" stroke="#fff" stroke-width="1.5"/></svg>
    </div>
    <p class="contact-text contact-text--email">hello@miriamholloway.com</p>

    <div class="contact-icon" style="top:238px">
      <svg viewBox="0 0 24 24" aria-hidden="true"><rect x="6" y="2" width="12" height="20" rx="2" fill="#000"/><rect x="7.5" y="4.5" width="9" height="13" fill="#fff"/><circle cx="12" cy="19.6" r="1" fill="#fff"/></svg>
    </div>
    <p class="contact-text contact-text--phone">+1 (555) 014 2290<br>+1 (555) 014 2290</p>

    <div class="contact-icon" style="top:303px">
      <svg viewBox="0 0 24 24" aria-hidden="true" fill="none" stroke="#000" stroke-width="1.2"><circle cx="12" cy="12" r="10.5"/><circle cx="12" cy="12" r="7"/><ellipse cx="12" cy="12" rx="3" ry="7"/><path d="M5 12h14M6 8.5h12M6 15.5h12M12 5v14"/></svg>
    </div>
    <p class="contact-text contact-text--web">www.miriamstrings.com</p>
  </section>

  <section class="card card--back">
    <div class="violin-art" role="img" aria-label="Yellow silhouette of a violin merged with a treble clef over diagonal music staff lines"></div>

    <div class="services">
      <h2 class="services__title">CALL IN FOR:</h2>
      <div class="service">
        <p class="service__name">PRIVATE VIOLIN LESSONS,</p>
        <p class="service__detail">(Primarily Classic)</p>
      </div>
      <div class="service">
        <p class="service__name">PERFORMANCE GIGS</p>
        <p class="service__detail">(Wedding, Birthday Parties<br>Funerals, Etc.)</p>
      </div>
      <div class="service">
        <p class="service__name">COLLABORATIONS WITH OTHER ARTISTS</p>
        <p class="service__detail">(Studio Recordings,<br>Performances)</p>
      </div>
    </div>
  </section>

</body>
</html>
```